Steadfast Carewell (02)

We're designing a website to sell Medicare Supplements. Attached is the content we want to say and general layout, but please use your best knowledge to make it better. This platform is intentionally simplistic because this is reaching an older demographic, so it should be very straightforward, attention-grabbing and extremely user-friendly, while still appearing reliable and professional.
This should be a two-page web design. The homepage has information on Medicare supplements (script in image attached below) along with a button to input zip code. This triggers a window to pop up asking for personal information (will also be listed in attachment).
This brings you to the second page that lists out the medicare supplement companies and plans based on inputed information. We just want to see the design you have in mind, so it doesn't matter what information you put in this section. Feel free to reference/replicate the information in image 3 in the doc. There should be a section where you can filter results by company, premium price, or coverage plans.
Target Market(s)
Seniors, 65+
Industry/Entity Type
Insurance
Number of Pages Required
2 page
Look and feel

```html
<!DOCTYPE html>
<html lang="en">
<head>
<meta charset="utf-8">
<title>Steadfast Carewell — Medicare Made Easy</title>
<link href="https://fonts.googleapis.com/css2?family=Raleway:wght@400;500;600;700;800&display=swap" rel="stylesheet">
<style>
  :root {
    --sky: #6aaac4;
    --paper: #f0f0f0;
    --white: #ffffff;
    --forest: #0e3d1c;
    --forest-btn: #0d4a1f;
    --mint: #8fcf9a;
    --teal: #2a6e8a;
    --teal-strong: #1f6b86;
    --ink: #1d2a24;
  }
  * { box-sizing: border-box; margin: 0; padding: 0; }
  html, body { width: 1200px; height: 2232px; overflow: hidden; }
  body { font-family: "Raleway", sans-serif; background: var(--paper); position: relative; }

  .callbar {
    height: 25px; background: var(--sky); color: var(--white);
    font-size: 14px; text-align: center; line-height: 25px;
  }
  .callbar strong { font-weight: 700; }

  .site-header { height: 83px; background: var(--paper); position: relative; }
  .brand {
    position: absolute; left: 170px; top: 30px;
    font-size: 21px; font-weight: 700; letter-spacing: 0.5px; color: var(--teal-strong);
  }

  .hero { position: relative; height: 678px; overflow: hidden; }
  .hero-photo {
    position: absolute; inset: 0;
    background:
      radial-gradient(ellipse at 45% 70%, rgba(200,170,160,0.55) 0%, rgba(200,170,160,0) 35%),
      radial-gradient(ellipse at 70% 10%, rgba(190,215,225,0.6) 0%, rgba(190,215,225,0) 40%),
      linear-gradient(160deg, #4f8fae 0%, #6aaac4 45%, #4a86a3 70%, #1d3550 100%);
  }
  .hero-content { position: absolute; inset: 0; text-align: center; color: var(--white); }
  .hero-title { position: absolute; left: 0; right: 0; top: 232px; font-size: 58px; font-weight: 700; line-height: 64px; }
  .hero-sub { position: absolute; left: 0; right: 0; top: 297px; font-size: 22px; font-weight: 400; line-height: 27px; }
  .zip-form { position: absolute; top: 377px; left: 385px; display: flex; gap: 8px; }
  .zip-input {
    width: 214px; height: 42px; border: none; border-radius: 5px;
    background: rgba(255,255,255,0.4); color: var(--white);
    font: 400 22px "Raleway", sans-serif; text-align: center;
  }
  .zip-input::placeholder { color: var(--white); }
  .find-btn {
    width: 214px; height: 42px; border: none; border-radius: 5px;
    background: var(--forest-btn); color: var(--mint);
    font: 700 21px "Raleway", sans-serif; letter-spacing: 2px;
  }

  .section-title { text-align: center; font-size: 37px; font-weight: 700; line-height: 44px; text-transform: uppercase; }

  .about { height: 676px; background: var(--paper); padding-top: 57px; }
  .about .section-title { color: var(--forest); }
  .lead { width: 760px; margin: 44px auto 0; text-align: center; font-size: 22.5px; line-height: 26.4px; color: var(--teal); }
  .lead strong { color: var(--teal-strong); font-weight: 700; }
  .benefits { list-style: none; position: relative; margin-left: 359px; width: 440px; }
  .benefits li { position: absolute; left: 0; width: 440px; display: flex; align-items: center; gap: 16px; font-size: 17.5px; line-height: 22px; color: var(--forest); }
  .benefits li svg { flex: none; }
  .benefits strong { font-weight: 700; }

  .costs { height: 744px; background: var(--sky); color: var(--white); padding-top: 64px; position: relative; }
  .costs .lead { color: var(--white); margin-top: 60px; width: 760px; }
  .costs .lead strong { color: var(--white); }
  .rating-cards { position: absolute; top: 398px; left: 245px; display: flex; gap: 16px; }
  .rating-card { width: 226px; height: 220px; background: var(--white); border-radius: 8px; padding: 14px 13px; color: var(--ink); }
  .rating-card h3 { font-size: 17px; font-weight: 800; line-height: 22px; color: var(--forest); text-transform: uppercase; margin-bottom: 6px; }
  .rating-card p { font-size: 14px; line-height: 17.6px; color: var(--forest); }
  .rating-note { position: absolute; top: 645px; left: 246px; width: 740px; font-size: 14px; line-height: 18px; }

  .site-footer { height: 26px; background: var(--paper); color: var(--teal-strong); font-size: 13px; line-height: 26px; text-align: right; padding-right: 174px; }
</style>
</head>
<body>
  <div class="callbar"><strong>CALL (800) 555-0142</strong> FOR MORE INFORMATION</div>

  <header class="site-header">
    <div class="brand">STEADFAST CAREWELL</div>
  </header>

  <section class="hero">
    <div class="hero-photo" role="img" aria-label="Photo of a smiling senior woman holding hands with a caregiver"></div>
    <div class="hero-content">
      <h1 class="hero-title">MEDICARE MADE EASY</h1>
      <p class="hero-sub">BE CONFIDENT IN CHOOSING THE MEDICARE SUPPLEMENT<br>PLAN THAT'S RIGHT FOR YOU</p>
      <form class="zip-form">
        <input class="zip-input" type="text" placeholder="ENTER ZIP CODE">
        <button class="find-btn" type="button">FIND PLANS</button>
      </form>
    </div>
  </section>

  <section class="about">
    <h2 class="section-title">What is a Medicare<br>Supplement Plan?</h2>
    <p class="lead">Each <strong>Medicare Supplement Insurance Plan</strong> offers a different level of basic benefits, but each lettered plan will include the same standardized basic benefits regardless of insurance company and location.<br><strong>Medicare Supplement Insurance Plans</strong> do not always cover vision, dental, long-term care, or hearing aids, but all plans must cover at least a portion of the following basic benefits:</p>
    <ul class="benefits">
      <li style="top:10px"><svg width="32" height="32" viewBox="0 0 32 32"><circle cx="16" cy="16" r="14" fill="none" stroke="#0e3d1c" stroke-width="3"/><circle cx="16" cy="16" r="8" fill="#0e3d1c"/></svg><span><strong>Medicare Part A Coinsurance</strong> costs up to an additional 365 days after Medicare benefits</span></li>
      <li style="top:78px"><svg width="32" height="32" viewBox="0 0 32 32"><circle cx="16" cy="16" r="14" fill="none" stroke="#0e3d1c" stroke-width="3"/><circle cx="16" cy="16" r="8" fill="#0e3d1c"/></svg><span><strong>Medicare Part A Hospice Care Coinsurance or Copayments</strong></span></li>
      <li style="top:147px"><svg width="32" height="32" viewBox="0 0 32 32"><circle cx="16" cy="16" r="14" fill="none" stroke="#0e3d1c" stroke-width="3"/><circle cx="16" cy="16" r="8" fill="#0e3d1c"/></svg><span><strong>Medicare Part B coinsurance or copayments</strong></span></li>
      <li style="top:230px"><svg width="32" height="32" viewBox="0 0 32 32"><circle cx="16" cy="16" r="14" fill="none" stroke="#0e3d1c" stroke-width="3"/><circle cx="16" cy="16" r="8" fill="#0e3d1c"/></svg><span>First three pints of blood used in a medical procedure</span></li>
    </ul>
  </section>

  <section class="costs">
    <h2 class="section-title">Medicare Supplement<br>Insurance Plan Costs</h2>
    <p class="lead">Although private insurance companies are required to offer the same basic benefits for each lettered plan, they do have the ability to charge different premiums.<br>You might want to shop around to find a <strong>Medicare Supplement Insurance Plan that may fit your medical and financial needs.</strong><br>Insurance companies may price their plan premiums in any of the following ways:</p>
    <div class="rating-cards">
      <article class="rating-card">
        <h3>Community<br>No-Age-Rated</h3>
        <p>These Medicare Supplement insurance plans charge premiums that are the same across the board, regardless of age.</p>
      </article>
      <article class="rating-card">
        <h3>Community<br>Issue-Age-Rated</h3>
        <p>These plans base their premiums on your age when you first enrolled in the policy.<br>Therefore, the younger you are when you enroll in this type of plan, the lower your premium will be.</p>
      </article>
      <article class="rating-card">
        <h3>Community<br>Attained-Age-Rated</h3>
        <p>Like issue-age-rated, these plans base their premiums on the age you were when you first bought a policy, but unlike issue-age-rated, premiums increase as you get older.</p>
      </article>
    </div>
    <p class="rating-note">Please note that no matter what rating method an insurance company uses, premiums may increase over time for reasons other than age, such as inflation.</p>
  </section>

  <footer class="site-footer">© 2020 STEADFAST CAREWELL SERVICES, INC.</footer>
</body>
</html>
```